Family business needs stationery redesign with new logo

Family owned company, established in 1987 wanting a brand 'refresh'. We are an electrical, refrigeration and construction company based in the Barkly Region Northern Territory, Australia. We have a new logo we would like to use which is uploaded along with our current letterhead and email signature. We are also dropping the word 'contractors' so please do not include this on any designs. Please note also, the 'orange' color used in our logo and designs should be Northern Territory red ochre which is as follows:

RGB (Hex): #C75B12
PantoneĀ® 159 C
CMYK: 1 / 74 / 100 / 7

We are needing our stationery redesigned using our new logo. Please include letterheads, business cards, envelopes, and email signatures.

We currently use our business letterheads for quotations, invoices, letters, HR matters, and internal memos.

We also need a separate simplified letterhead for internal paperwork such as employee leave forms, meeting agendas, and meeting minutes etc.
Updates

Reason: Needing more submissions of full package designs. We are wanting all our stationery, including business cards, letterheads, email signatures, envelopes, etc to be cohesive. We also require ALL the information, as supplied on our template letterhead, to be included on the new letterhead designs. including electrical license no.etc Thank you, K&M

Reason: needing more time as work has got in the way of looking over designs. A lot of designs not meeting the brief/criteria.

Industry/Entity Type

Business

Colors
0355a3
f37122

Requirements
Must have
• The 'orange' color used in the designs should be Northern Territory red ochre which is as follows:
• RGB (Hex): #C75B12
• PantoneĀ® 159 C
• CMYK: 1 / 74 / 100 / 7
• ***MUST INCLUDE ALL INFORMATION THAT IS ON OUR CURRENT LETTERHEAD***
Should not have
• Please do not include the word 'contractors'

```html
<!DOCTYPE html>
<html lang="en">
<head>
<meta charset="utf-8">
<title>K&amp;M Stationery Set</title>
<link href="https://fonts.googleapis.com/css2?family=Open+Sans:wght@400;600;700;800&display=swap" rel="stylesheet">
<style>
  :root {
    --navy: #24306b;
    --ochre: #c75b12;
    --paper: #ffffff;
    --backdrop: #ece7df;
    --ink: #24306b;
  }
  * { box-sizing: border-box; margin: 0; padding: 0; }
  html, body { width: 1200px; height: 1200px; overflow: hidden; }
  body { background: var(--backdrop); font-family: "Open Sans", Arial, sans-serif; position: relative; }

  .sheet { position: absolute; background: var(--paper); box-shadow: 0 6px 18px rgba(0,0,0,.15); overflow: hidden; }

  /* brand name lockup */
  .brand-name { font-weight: 800; color: var(--navy); letter-spacing: 1px; line-height: 1; }
  .abn { color: var(--ochre); font-size: 13px; }

  /* vertical rule with trailing dashes */
  .rule { position: absolute; display: flex; flex-direction: column; align-items: center; }
  .rule .bar { background: var(--navy); border-radius: 4px; }
  .rule .dash { background: var(--ochre); border-radius: 4px; }

  /* Letterhead */
  .letterhead { left: 50px; top: 280px; width: 460px; height: 650px; }
  .letterhead .rule { left: 28px; top: 40px; gap: 10px; }
  .letterhead .bar { width: 8px; height: 410px; }
  .letterhead .dash.d1 { width: 8px; height: 58px; }
  .letterhead .dash.d2 { width: 8px; height: 20px; }
  .letterhead .dash.d3 { width: 8px; height: 14px; }
  .letterhead .dash.d4 { width: 8px; height: 9px; }
  .letterhead .lockup { position: absolute; left: 70px; top: 50px; text-align: center; width: 150px; }
  .letterhead .brand-name { font-size: 42px; }
  .letterhead .abn { display: block; margin-top: 12px; }
  .letterhead .faint-name { position: absolute; left: 110px; top: 260px; font-size: 120px; font-weight: 800; color: var(--navy); opacity: .04; }
  .letterhead .footer { position: absolute; left: 0; right: 0; bottom: 0; }
  .letterhead .footer .stripe { height: 6px; background: var(--ochre); }
  .letterhead .footer .band { height: 58px; background: var(--navy); color: #fff; font-size: 8px; display: flex; align-items: center; justify-content: center; gap: 12px; padding-top: 6px; }

  /* Business card front */
  .card { width: 300px; height: 170px; }
  .card-front { left: 560px; top: 80px; background: var(--navy); }
  .card-front .topline { position: absolute; top: 26px; left: 14px; right: 14px; display: flex; align-items: center; gap: 5px; }
  .card-front .topline .dash { height: 3px; width: 8px; background: var(--ochre); border-radius: 2px; }
  .card-front .topline .dash.long { width: 30px; }
  .card-front .topline .line { flex: 1; height: 3px; background: #fff; border-radius: 2px; }
  .card-front .lockup { position: absolute; left: 0; right: 0; top: 62px; text-align: center; }
  .card-front .brand-name { color: #fff; font-size: 44px; }
  .card-front .abn { color: #fff; display: block; margin-top: 10px; font-size: 12px; }

  /* Business card back */
  .card-back { left: 880px; top: 80px; }
  .card-back .rule { left: 12px; top: 12px; gap: 5px; }
  .card-back .bar { width: 3px; height: 92px; }
  .card-back .dash.d1 { width: 3px; height: 34px; }
  .card-back .dash.d2 { width: 3px; height: 8px; }
  .card-back .dash.d3 { width: 3px; height: 6px; }
  .card-back .dash.d4 { width: 3px; height: 4px; }
  .card-back .lockup { position: absolute; left: 28px; top: 24px; width: 80px; text-align: center; }
  .card-back .brand-name { font-size: 24px; }
  .card-back .abn { display: block; margin-top: 10px; font-size: 12px; }
  .card-back .corner { position: absolute; right: 0; top: 0; }
  .card-back .person { position: absolute; left: 176px; top: 24px; }
  .card-back .person .name { color: var(--ochre); font-size: 13px; text-transform: uppercase; }
  .card-back .person .role { color: var(--navy); font-size: 4.5px; font-weight: 700; text-transform: uppercase; letter-spacing: .2px; }
  .card-back .contact { position: absolute; left: 176px; top: 112px; font-size: 6px; color: var(--navy); line-height: 1.6; }
  .card-back .web { position: absolute; left: 24px; top: 144px; font-size: 6px; color: var(--navy); }
  .label { color: var(--ochre); }

  /* Envelope */
  .envelope { left: 560px; top: 300px; width: 600px; height: 300px; border-radius: 24px 24px 0 0; }
  .envelope .flap { position: absolute; left: 0; right: 0; top: 0; height: 90px; background: var(--ochre); }
  .envelope .rule { left: 28px; top: 120px; gap: 7px; }
  .envelope .bar { width: 6px; height: 110px; }
  .envelope .dash.d1 { width: 6px; height: 40px; }
  .envelope .dash.d2 { width: 6px; height: 14px; }
  .envelope .dash.d3 { width: 6px; height: 10px; }
  .envelope .dash.d4 { width: 6px; height: 7px; }
  .envelope .lockup { position: absolute; left: 60px; top: 150px; width: 130px; text-align: center; }
  .envelope .brand-name { font-size: 40px; }
  .envelope .abn { display: block; margin-top: 8px; }
  .envelope .contact { position: absolute; left: 56px; top: 222px; font-size: 12px; color: var(--navy); line-height: 1.45; }
</style>
</head>
<body>

  <section class="sheet letterhead" aria-label="Letterhead">
    <div class="rule">
      <span class="bar"></span><span class="dash d1"></span><span class="dash d2"></span><span class="dash d3"></span><span class="dash d4"></span>
    </div>
    <div class="lockup">
      <span class="brand-name">K&amp;M</span>
      <span class="abn">ABN 73</span>
    </div>
    <div class="faint-name" aria-hidden="true">K&amp;M</div>
    <footer class="footer">
      <div class="stripe"></div>
      <div class="band">
        <span>Address: PO Box 4410, 52 Ridge St, Banka Creek NT 0862</span>
        <span>Ph: 08 7741</span>
        <span>Cell: 0455</span>
        <span>Email: info@kmbuild.com.au</span>
      </div>
    </footer>
  </section>

  <section class="sheet card card-front" aria-label="Business card front">
    <div class="topline">
      <span class="dash"></span><span class="dash"></span><span class="dash long"></span><span class="line"></span>
    </div>
    <div class="lockup">
      <span class="brand-name">K&amp;M</span>
      <span class="abn">ABN 73</span>
    </div>
  </section>

  <section class="sheet card card-back" aria-label="Business card back">
    <svg class="corner" width="80" height="90" viewBox="0 0 80 90" aria-hidden="true">
      <path d="M0 0 H80 V0 C80 45 55 75 20 88 C45 65 55 35 35 0 Z" fill="#c75b12"/>
    </svg>
    <div class="rule">
      <span class="bar"></span><span class="dash d1"></span><span class="dash d2"></span><span class="dash d3"></span><span class="dash d4"></span>
    </div>
    <div class="lockup">
      <span class="brand-name">K&amp;M</span>
      <span class="abn">ABN 73</span>
    </div>
    <div class="person">
      <div class="name">Dana</div>
      <div class="role">Corporate Services Manager</div>
    </div>
    <div class="contact">
      <div><span class="label">Address:</span> PO Box 4410, 52 Ridge St,<br>&nbsp;&nbsp;&nbsp;&nbsp;&nbsp;&nbsp;&nbsp;&nbsp;&nbsp;&nbsp;Banka Creek NT 0862</div>
      <div><span class="label">Ph:</span> 08 7741&nbsp;&nbsp; <span class="label">Cell:</span> 0455</div>
      <div><span class="label">Email:</span> info@kmbuild.com.au</div>
    </div>
    <div class="web"><span class="label">Web:</span> www.kmbuild.com.au</div>
  </section>

  <section class="sheet envelope" aria-label="Envelope">
    <div class="flap"></div>
    <div class="rule">
      <span class="bar"></span><span class="dash d1"></span><span class="dash d2"></span><span class="dash d3"></span><span class="dash d4"></span>
    </div>
    <div class="lockup">
      <span class="brand-name">K&amp;M</span>
      <span class="abn">ABN 73</span>
    </div>
    <div class="contact">
      <div><span class="label">Address:</span> PO Box 4410, 52 Ridge St, Banka Creek NT 0862</div>
      <div><span class="label">Ph:</span> 08 7741</div>
      <div><span class="label">Cell:</span> 0455</div>
      <div><span class="label">Email:</span> info@kmbuild.com.au</div>
    </div>
  </section>

</body>
</html>
```